Varlow's Electrical & Solar - Business Cards

I want my business card to stand out from the rest. I will provide my business name logo and my icon logo to be implemented onto the card.

On the front of the card, can i have the following. Just make it neat & professional please.

Dean Harrop
varlowselectrical@mailbox-example.net
0491 837 562
ABN: 41 269 507 813
License No. 582146K
FREE QUOTES
24/7 Emergency

On the back of the card, can I have "Our Services" and maybe add the V logo on the back in the background or something. Under "Our Services" I want the following:

LED Lighting Upgrades
Switches & Outlets
Smoke Alarms
Switchboard Upgrades
Fault Finding
Rewiring
New Builds
Test & Tagging
All Electrical Maintenance & Repairs

Can you guys add the instagram logo and next to it, put varlows_electrical

Can you guys also add the facebook logo and next to it put Varlow's Electrical & Solar. Make sure the instagram & facebook icon is in either white, green or black.

Also I have put down double sided, not sure why when i save it, it keeps going to single sided. I need my business card double sided.

New Customers

Dean Harrop varlowselectrical@mailbox-example.net 0491 837 562 ABN: 41 269 507 813 License No. 582146K FREE QUOTES 24/7 Emergency

• must be tidy, professional and appealing

```html
<!DOCTYPE html>
<html lang="en">
<head>
<meta charset="utf-8">
<title>Varlow's Electrical &amp; Solar – Business Cards</title>
<link rel="stylesheet" href="https://fonts.googleapis.com/css2?family=Montserrat:wght@400;500;700&display=swap">
<style>
  :root {
    --stage: #7a6148;
    --card: #161616;
    --green: #2aa34a;
    --green-soft: #5cc15e;
    --text: #ffffff;
  }
  * { margin: 0; padding: 0; box-sizing: border-box; }
  html, body { width: 900px; height: 1200px; overflow: hidden; }
  body {
    position: relative;
    background: var(--stage);
    font-family: "Montserrat", Arial, sans-serif;
    color: var(--text);
  }
  .card {
    position: absolute;
    left: 78px;
    width: 744px;
    height: 442px;
    background: var(--card);
    border-radius: 30px;
  }
  .card--front { top: 130px; }
  .card--back { top: 637px; }

  .brand-mark {
    position: absolute;
    border: 8px solid var(--green);
    border-radius: 50%;
    display: flex;
    align-items: center;
    justify-content: center;
    text-align: center;
    color: var(--green);
    font-weight: 700;
    line-height: 1.25;
  }
  .card--front .brand-mark { left: 68px; top: 100px; width: 244px; height: 244px; font-size: 22px; padding: 0 30px; }
  .card--back .brand-mark { left: 32px; top: 81px; width: 280px; height: 280px; font-size: 25px; padding: 0 34px; }

  .divider {
    position: absolute;
    width: 2px;
    background: var(--green);
  }
  .card--front .divider { left: 346px; top: 92px; height: 260px; }
  .card--back .divider { left: 333px; top: 71px; height: 300px; }

  .details { position: absolute; left: 378px; top: 88px; }
  .details__name { font-size: 28px; font-weight: 700; color: var(--green); margin-bottom: 34px; }
  .details__line { display: flex; align-items: center; font-size: 19px; font-weight: 500; height: 30px; }
  .details__line--email { font-size: 15.5px; }
  .details__line svg { width: 18px; height: 18px; margin-right: 6px; fill: var(--green); flex: none; }
  .details__label { color: var(--green); font-weight: 700; margin-right: 5px; }
  .details__gap { height: 3px; }
  .social-dot { width: 18px; height: 18px; background: var(--green); border-radius: 3px; margin-right: 12px; flex: none; }
  .details__offer { margin-top: 17px; font-size: 18.5px; font-weight: 500; }

  .services { position: absolute; left: 354px; top: 68px; }
  .services__title { font-size: 29px; font-weight: 700; color: var(--green); margin-bottom: 8px; }
  .services__list { list-style: none; }
  .services__list li { display: flex; align-items: center; font-size: 19px; font-weight: 500; height: 29px; }
  .services__list li::before {
    content: ""; width: 9px; height: 9px; border-radius: 50%;
    background: var(--green); margin: 0 9px 0 4px; flex: none;
  }
</style>
</head>
<body>
  <section class="card card--front" aria-label="Business card front">
    <div class="brand-mark">Varlow's Electrical &amp; Solar</div>
    <div class="divider"></div>
    <div class="details">
      <p class="details__name">Dean Harrop</p>
      <p class="details__line">
        <svg viewBox="0 0 24 24" aria-hidden="true"><path d="M3 9c0-3 4-5 9-5s9 2 9 5v2h-5V9c-1-.6-2.5-1-4-1s-3 .4-4 1v2H3zM6 12h12l2 8H4z"/></svg>0491 837 562
      </p>
      <p class="details__line details__line--email">
        <svg viewBox="0 0 24 24" aria-hidden="true"><path d="M3 6h18v2l-9 5-9-5zM3 10l9 5 9-5v8H3z"/></svg>varlowselectrical@mailbox-example.net
      </p>
      <div class="details__gap"></div>
      <p class="details__line"><span class="details__label">ABN:</span>41 269 507 813</p>
      <p class="details__line"><span class="details__label">License No:</span>582146K</p>
      <p class="details__line"><span class="social-dot"></span>Varlow's Electrical &amp; Solar</p>
      <p class="details__offer">FREE QUOTES 24/7 Emergency</p>
    </div>
  </section>

  <section class="card card--back" aria-label="Business card back">
    <div class="brand-mark">Varlow's Electrical &amp; Solar</div>
    <div class="divider"></div>
    <div class="services">
      <h2 class="services__title">Our Services</h2>
      <ul class="services__list">
        <li>LED Lighting Upgrades</li>
        <li>Switches &amp; Outlets</li>
        <li>Smoke Alarms</li>
        <li>Switchboard Upgrades</li>
        <li>Fault Finding</li>
        <li>Rewiring</li>
        <li>New Builds</li>
        <li>Test &amp; Tagging</li>
        <li>All Electrical Maintenance &amp; Repairs</li>
      </ul>
    </div>
  </section>
</body>
</html>
```